Eye-Catching, Direct Marketing Residential Painting Flyer!

I am run a residential painting business and am looking for a flyer to be designed to mailout to potential customers.
I want the copy/wording to be designed similar to this flyer.

It's important that the person reading the flyer gets the benefits we're promoting which is why I want the wording/copy to be almost identical to the flyer attached.

However, the structure will be different. The flyer will be a postcard thick, 5 x11.5.
Double sided.

The name of the company is Brightwall Coaters.

I would also like the prominent colour to either be light green or orange.

Target Market(s)

Home Owners between the age of 45-80.

Industry/Entity Type

Painting And Decorating

Font styles to use
Serif

Colors
f68d4d
faa54b
f78f20
f37122
9bcb3c
abd037
cadf82

Requirements
Must have
• Excellent Eye-Catching Design
• Benefits Visibly Promoted
• Action Taking Incentive- Call Now for FREE Window Cleaning and FREE Painting Estimate
Should not have
• Crowded wording

```html
<!DOCTYPE html>
<html lang="en">
<head>
<meta charset="utf-8">
<title>Brightwall Coaters – Door Hanger Flyer</title>
<link rel="stylesheet" href="https://fonts.googleapis.com/css2?family=Archivo+Black&family=Anton&family=Ubuntu:wght@500&family=Open+Sans:ital,wght@0,400;0,600;1,600&display=swap">
<style>
:root{
  --bg:#93b8d4;
  --green:#a6c93a;
  --blue:#1b73bb;
  --orange:#f8a428;
  --maroon:#a0205a;
  --crimson:#a31f34;
  --magenta:#d81b72;
  --sky:#27a3dc;
  --ink:#444;
  --white:#fff;
}
*{margin:0;padding:0;box-sizing:border-box}
html,body{width:1200px;height:1200px;overflow:hidden}
body{background:var(--bg);position:relative;font-family:"Open Sans",sans-serif}
.panel{position:absolute;top:102px;width:434px;height:996px}
.panel--front{left:110px}
.panel--back{left:642px}
.panel__shape{position:absolute;left:0;top:0}
.abs{position:absolute}

/* front */
.headline{left:0;width:434px;top:56px;text-align:center;font-family:"Archivo Black",sans-serif;color:var(--white);font-size:34px;line-height:38px}
.concerns{left:27px;top:172px;font-family:"Ubuntu",sans-serif;font-weight:500;font-size:22px;line-height:27.2px;color:var(--blue)}
.concerns .o{color:var(--orange)}
.concerns .g{color:var(--green)}
.concerns .r{color:var(--crimson)}
.concerns .s{color:var(--sky)}
.concerns .m{color:var(--magenta)}
.promise{left:10px;width:414px;top:468px;text-align:center;font-family:"Archivo Black",sans-serif;color:var(--white);font-size:21.5px;line-height:27.5px}
.offer-title{left:0;width:434px;top:568px;text-align:center;font-family:"Anton",sans-serif;color:var(--maroon);font-size:28px;line-height:36px}
.offer{left:12px;width:410px;border:1px dashed var(--maroon);text-align:center;color:var(--maroon);font-size:11px;line-height:14.5px;padding-top:4px}
.offer--window{top:610px;height:56px}
.offer--design{top:675px;height:69px}
.offer strong{font-style:italic;font-weight:600;text-transform:uppercase}
.estimate{left:0;width:434px;top:756px;text-align:center;font-family:"Anton",sans-serif;color:var(--orange);font-size:36px;line-height:42px}
.phone{left:0;width:434px;top:795px;text-align:center;font-family:"Anton",sans-serif;color:var(--blue);font-size:40px;line-height:46px}
.brand{left:0;width:434px;top:868px;display:flex;justify-content:center;align-items:center;gap:8px}
.brand__mark{width:14px;height:14px;background:var(--blue)}
.brand__name{font-family:"Anton",sans-serif;font-size:30px;color:var(--blue);letter-spacing:1px}
.links{left:0;width:434px;top:960px;display:flex;justify-content:center;gap:14px;font-family:"Ubuntu",sans-serif;font-weight:500;font-size:13.5px;color:var(--green)}
.links span{display:flex;align-items:center;gap:4px}
.links i{display:inline-block;width:11px;height:11px;background:var(--blue);border-radius:50%}
.links i.sq{border-radius:2px}

/* back */
.back-title{left:0;width:434px;top:50px;text-align:center;font-family:"Anton",sans-serif;color:var(--white);font-size:32px;line-height:40px}
.label{left:26px;font-size:13px;font-weight:600;line-height:16px}
.label--problem{color:var(--blue)}
.label--solution{color:var(--green)}
.copy{left:26px;width:382px;font-size:10px;line-height:14.2px;color:var(--ink);text-align:justify}
.copy b{font-weight:600}
.caption{font-size:10.5px;font-weight:600;color:#222}
.photo{position:absolute}
.quote{left:26px;width:382px;font-size:10.5px;line-height:14.4px;color:var(--blue);font-style:italic;font-weight:600}
.quote .who{color:var(--green);font-style:normal}
.arrow{position:absolute}
</style>
</head>
<body>

<section class="panel panel--front">
  <svg class="panel__shape" width="434" height="996" viewBox="0 0 434 996" aria-hidden="true">
    <rect x="0" y="54" width="434" height="942" fill="#fff"/>
    <polygon points="0,54 218,0 434,54" fill="var(--green)"/>
    <rect x="10" y="50" width="414" height="116" fill="var(--green)"/>
    <path d="M242 166 L424 166 L424 200 Q424 218 409 218 Q394 218 394 200 L394 192 Q394 180 380 180 L352 180 L352 270 Q352 295 326 295 Q300 295 300 270 L300 200 Q300 186 285 186 L262 186 Q242 186 242 166 Z" fill="var(--green)"/>
    <path d="M276 458 V375 A74 74 0 0 1 424 375 V458 Z" fill="var(--blue)"/>
    <rect x="10" y="458" width="414" height="100" fill="var(--blue)"/>
    <rect x="10" y="558" width="414" height="5" fill="var(--orange)"/>
    <text x="350" y="446" text-anchor="middle" font-family="Archivo Black, sans-serif" font-size="150" fill="var(--orange)">?</text>
    <rect x="0" y="986" width="434" height="10" fill="var(--orange)"/>
  </svg>

  <h1 class="abs headline">TAKE<br>CONTROL OF HOW<br>YOUR HOME LOOKS</h1>

  <p class="abs concerns">
    DOES YOUR<br>
    DECK INTERIOR<br>
    <span class="o">SIDING</span><br>
    WALLS<br>
    FENCE<br>
    WINDOWS<br>
    <span class="g">LOOK FADED,</span><br>
    <span class="r">DIRTY, OUT OF DATE,</span><br>
    ARE THEY <span class="s">CHIPPING</span><br>
    OR <span class="m">PEELING</span>
  </p>

  <p class="abs promise">WE MAKE YOUR HOME LOOK<br>CLEAN, FRESH &amp; BEAUTIFULL<br>AGAIN</p>

  <h2 class="abs offer-title">Special Offer!</h2>
  <div class="abs offer offer--window">If you are one of the<br><strong>First 17 exterior projects</strong><br>that book with us, you will receive a complimentary window cleaning!</div>
  <div class="abs offer offer--design">If you are one of the<br><strong>First 17 exterior projects</strong><br>that book with us, you will receive a complimentary interior design<br>consultation by a professional interior designer!</div>

  <p class="abs estimate">FREE ESTIMATES:</p>
  <p class="abs phone">555-014-2736</p>

  <div class="abs brand"><span class="brand__mark"></span><span class="brand__name">BRIGHTWALL COATERS</span></div>

  <div class="abs links">
    <span><i></i>brightwallcoaters.com</span>
    <span><i class="sq"></i>social: /brightwallcoaters</span>
  </div>
</section>

<section class="panel panel--back">
  <svg class="panel__shape" width="434" height="996" viewBox="0 0 434 996" aria-hidden="true">
    <rect x="0" y="54" width="434" height="942" fill="#fff"/>
    <polygon points="0,54 218,0 434,54" fill="var(--green)"/>
    <rect x="0" y="50" width="434" height="49" fill="var(--green)"/>
    <path d="M330 99 L434 99 L434 116 Q434 126 422 126 Q410 126 410 116 L410 112 Q400 108 385 112 L385 138 Q385 150 373 150 Q362 150 362 138 L362 114 Q358 110 358 114 L358 126 Q358 136 348 136 Q338 136 338 126 L338 110 Q338 99 330 99 Z" fill="var(--green)"/>
    <rect x="0" y="986" width="434" height="10" fill="var(--orange)"/>
  </svg>

  <h2 class="abs back-title">Problems &amp; Solutions</h2>

  <p class="abs label label--problem" style="top:106px">Problem</p>
  <p class="abs copy" style="top:124px">Your deck or fence is chipping or peeling,and looks old and faded.</p>
  <p class="abs label label--solution" style="top:142px">Solution</p>
  <p class="abs copy" style="top:159px">A fresh coat of stain will protect your investment and make it look clean, fresh and Beautiful again !</p>

  <p class="abs caption" style="left:24px;top:193px">Problem</p>
  <p class="abs caption" style="left:300px;top:193px">Solution</p>
  <div class="photo" role="img" aria-label="Weathered wooden deck steps before staining" style="left:26px;top:212px;width:106px;height:108px;background:linear-gradient(160deg,#8a7a66,#b9ad9c 55%,#d2c7b6)"></div>
  <svg class="arrow" style="left:182px;top:240px" width="70" height="52" viewBox="0 0 70 52" aria-hidden="true"><rect x="0" y="11" width="2.5" height="30" fill="var(--blue)"/><rect x="4.5" y="11" width="2.5" height="30" fill="var(--blue)"/><rect x="9" y="11" width="2.5" height="30" fill="var(--blue)"/><rect x="13" y="11" width="35" height="30" fill="var(--blue)"/><polygon points="48,0 70,26 48,52" fill="var(--blue)"/></svg>
  <div class="photo" role="img" aria-label="Freshly stained grey deck with white railing" style="left:302px;top:212px;width:106px;height:108px;background:linear-gradient(170deg,#9da3a6,#7f8487 60%,#676b6d)"></div>

  <p class="abs quote" style="top:326px">“We would be happy to recommend them !” - <span class="who">Tomas &amp; Elise - Elm Ridge</span></p>

  <p class="abs label label--problem" style="top:344px">Problem</p>
  <p class="abs copy" style="top:361px">Your exterior windows, doors, <b>Garage Doors, Stucco, Siding, Soffits</b> are chipping or peeling, and look</p>
  <p class="abs label label--solution" style="top:396px">Solution</p>
  <p class="abs copy" style="top:413px">A fresh coat of stain will protect your investment and make it look fresh and Beautiful again! clean,</p>

  <div class="photo" role="img" aria-label="Brick house front with worn trim before painting" style="left:26px;top:448px;width:151px;height:98px;background:linear-gradient(180deg,#c9cdd0,#7a4d3c 45%,#5b6e42)"></div>
  <svg class="arrow" style="left:182px;top:471px" width="70" height="52" viewBox="0 0 70 52" aria-hidden="true"><rect x="0" y="11" width="2.5" height="30" fill="var(--blue)"/><rect x="4.5" y="11" width="2.5" height="30" fill="var(--blue)"/><rect x="9" y="11" width="2.5" height="30" fill="var(--blue)"/><rect x="13" y="11" width="35" height="30" fill="var(--blue)"/><polygon points="48,0 70,26 48,52" fill="var(--blue)"/></svg>
  <div class="photo" role="img" aria-label="Same brick house with freshly painted white trim" style="left:256px;top:448px;width:152px;height:98px;background:linear-gradient(180deg,#dfe2e4,#8b4a3a 45%,#5f7a40)"></div>

  <p class="abs quote" style="top:555px">“This is deffinitely best paint jb and I would not hesitate to recommend Brightwall Coaters!” - <span class="who">Ruth &amp; Omar - Maple Heights</span></p>

  <p class="abs label label--problem" style="top:591px">Problem</p>
  <p class="abs copy" style="top:608px">Is the colour in your interior basement, kitchen, bedrooms and bathrooms walls, doors, and trim faded or out-of-date ?</p>
  <p class="abs label label--solution" style="top:637px">Solution</p>
  <p class="abs copy" style="top:654px">A fresh coat of paint to make your interior look clean, fresh and beautiful again!</p>

  <div class="photo" role="img" aria-label="Room with orange walls and wainscoting during repainting" style="left:26px;top:687px;width:151px;height:97px;background:linear-gradient(90deg,#b86a2e,#d99a5a 55%,#e9e4da)"></div>
  <svg class="arrow" style="left:182px;top:709px" width="70" height="52" viewBox="0 0 70 52" aria-hidden="true"><rect x="0" y="11" width="2.5" height="30" fill="var(--blue)"/><rect x="4.5" y="11" width="2.5" height="30" fill="var(--blue)"/><rect x="9" y="11" width="2.5" height="30" fill="var(--blue)"/><rect x="13" y="11" width="35" height="30" fill="var(--blue)"/><polygon points="48,0 70,26 48,52" fill="var(--blue)"/></svg>
  <div class="photo" role="img" aria-label="Same room repainted in soft grey with white wainscoting" style="left:257px;top:687px;width:151px;height:97px;background:linear-gradient(180deg,#a9a6a5,#cfccc9 60%,#5a4a40)"></div>

  <p class="abs quote" style="top:792px">“I am 150% satisfied with the quality of work!” <span class="who">Paula &amp; Henrik - Elm Ridge</span></p>

  <p class="abs label label--problem" style="top:811px">Problem</p>
  <p class="abs copy" style="top:828px">Your exterior semi-transparent deck, fence or siding is peeling, chipping or faded.</p>
  <p class="abs label label--solution" style="top:843px">Solution</p>
  <p class="abs copy" style="top:860px">A fresh coat of stain to protect the wood and make it look clean, fresh and beautiful!</p>

  <p class="abs quote" style="top:901px;width:194px;text-align:justify">“They provided us with the satisfaction that we chose wisely when we decided to grant the project to this company”<br><span class="who">Linda &amp; Marcus - Elm Ridge</span></p>
  <div class="photo" role="img" aria-label="Wooden deck boards half stained in rich reddish brown" style="left:256px;top:882px;width:152px;height:93px;background:linear-gradient(120deg,#9b8f7e,#7a3a24 55%,#5c2a1a)"></div>
</section>

</body>
</html>
```